Business card with professional look

I would like a creative yet professional looking business card for our business. We sell broadcast TV related security products for mobile phones, set top boxes, and tablets. Our customers are international. We have a logo we like and I would like to possibly add some color to the business card but keep it professional looking.

Target Market(s)

Professionals in the TV, cable, ans Satellite industries

Industry/Entity Type

Cable Tv

Contact Information for Business Card

Name Ned Vastermill, title CEO, Address 8130 Harborline Court, Suite 400, Del Arvo, CA 91584 USA, phone numbers m:+1.619.284.7302 o:+1.855.672.9140, email, logo

Font styles to use
Other font styles liked:
• Open to any font that looks good with logo

Requirements
Must have
• professional look with colors coordinated with logo colors. would like to add one or two different colors as well as some form of background color

```html
<!DOCTYPE html>
<html lang="en">
<head>
<meta charset="utf-8">
<title>Vantaro Business Card</title>
<link rel="stylesheet" href="https://fonts.googleapis.com/css2?family=Roboto:wght@400;500;700&display=swap">
<style>
  :root {
    --backdrop: #d6d6d6;
    --card-paper: #f4f4f4;
    --band-dark: #2a2a2a;
    --accent-blue: #1b7fd6;
    --logo-ink: #3a3a3a;
    --name-grey: #8d8d8d;
    --text-light: #f2f2f2;
    --texture-grey: #e6e6e6;
  }
  * { margin: 0; padding: 0; box-sizing: border-box; }
  html, body {
    width: 1200px; height: 900px; overflow: hidden;
    background: var(--backdrop);
    font-family: "Roboto", Arial, sans-serif;
  }
  .business-card {
    position: absolute; left: 180px; top: 210px;
    width: 840px; height: 480px;
    background: var(--card-paper);
    overflow: hidden;
    box-shadow: 0 6px 18px rgba(0,0,0,0.18);
  }
  .card-shapes { position: absolute; inset: 0; }
  .paper-texture {
    position: absolute; background: var(--texture-grey);
  }
  .paper-texture.left { left: 0; top: 0; width: 120px; height: 60px; }
  .paper-texture.right { right: 0; top: 90px; width: 310px; height: 120px; }
  .brand {
    position: absolute; left: 210px; top: 62px;
    display: flex; align-items: center; gap: 14px;
  }
  .brand-name {
    font-size: 52px; font-weight: 700; color: var(--logo-ink);
    letter-spacing: -1px;
  }
  .brand-mark {
    width: 44px; height: 44px; background: var(--accent-blue);
  }
  .holder {
    position: absolute; left: 70px; top: 225px;
  }
  .holder-name {
    display: flex; align-items: center; gap: 14px;
    font-size: 32px; font-weight: 700; color: var(--name-grey);
  }
  .holder-title {
    margin-left: 34px; margin-top: 2px;
    font-size: 17px; color: var(--text-light);
  }
  .contact-list {
    position: absolute; left: 455px; top: 268px;
    list-style: none; color: var(--text-light);
    font-size: 18px; line-height: 1.25;
  }
  .contact-list li {
    display: flex; gap: 14px; align-items: flex-start; margin-bottom: 10px;
  }
  .contact-icon { width: 18px; height: 18px; flex: none; margin-top: 3px; }
</style>
</head>
<body>
  <div class="business-card">
    <div class="paper-texture left" role="img" aria-label="Subtle diagonal paper texture"></div>
    <div class="paper-texture right" role="img" aria-label="Subtle diagonal paper texture"></div>

    <svg class="card-shapes" width="840" height="480" viewBox="0 0 840 480">
      <path d="M0 165 L360 165 C400 165 410 215 450 215 L840 215 L840 480 L0 480 Z" fill="var(--band-dark)"/>
      <path d="M0 165 L360 165 C400 165 410 215 450 215 L840 215" fill="none" stroke="var(--accent-blue)" stroke-width="4"/>
    </svg>

    <div class="brand">
      <span class="brand-name">Vantaro</span>
      <span class="brand-mark"></span>
    </div>

    <div class="holder">
      <div class="holder-name">
        <svg class="contact-icon" viewBox="0 0 20 20" fill="var(--accent-blue)"><circle cx="10" cy="6" r="4.5"/><path d="M2 19c0-5 3.5-7 8-7s8 2 8 7z"/></svg>
        Ned Vastermill
      </div>
      <div class="holder-title">CEO</div>
    </div>

    <ul class="contact-list">
      <li>
        <svg class="contact-icon" viewBox="0 0 20 20" fill="var(--accent-blue)"><path d="M4 2l3 0 1.5 4-2 1.5c1 2 2.5 3.5 4.5 4.5l1.5-2 4 1.5 0 3c0 1-1 2-2 2C8 17 3 12 2 4c0-1 1-2 2-2z"/></svg>
        <span>m:+1.619.284.7302<br>o:+1.855.672.9140</span>
      </li>
      <li>
        <svg class="contact-icon" viewBox="0 0 20 20" fill="var(--accent-blue)"><rect x="1" y="4" width="18" height="12" rx="1"/><path d="M2 5l8 6 8-6" fill="none" stroke="var(--band-dark)" stroke-width="1.5"/></svg>
        <span>ned@vantaro-mail.com</span>
      </li>
      <li>
        <svg class="contact-icon" viewBox="0 0 20 20" fill="none" stroke="var(--accent-blue)" stroke-width="1.8"><circle cx="10" cy="10" r="8"/><ellipse cx="10" cy="10" rx="3.5" ry="8"/><path d="M2 10h16"/></svg>
        <span>www.vantaro-mail.com</span>
      </li>
      <li>
        <svg class="contact-icon" viewBox="0 0 20 20" fill="var(--accent-blue)"><path d="M10 1a6 6 0 0 0-6 6c0 5 6 12 6 12s6-7 6-12a6 6 0 0 0-6-6z"/><circle cx="10" cy="7" r="2.2" fill="var(--band-dark)"/></svg>
        <span>8130 Harborline Court,<br>Suite 400, Del Arvo,<br>CA 91584 USA</span>
      </li>
    </ul>
  </div>
</body>
</html>
```